Business Card Design Project

Shop and office fit out company wants to attract new customers by focusing on the repairs and maintenance side of the business.
We are known for our reliable and professional service and the idea is to hand out these business cards to potential customers in shopping centres or offices. The business card needs to be interesting and inviting enough to make people notice and calling us if our services are required.

Target Market(s)

30-50 year old shop managers or business owners. People looking for a good deal. ie. good value for money.

Industry/Entity Type

Professional Service

Requirements
Must have
• Use both sides of card.

Main Title: Fitout Care Repairs

At the bottom of the card; A division of Bramble Fitouts Australia Pty Ltd

Services:
Joinery metalwork and fixture repairs
Patching and painting
Lighting replacement
Fast reliable service
20 years experience
Fully insured
100% workmanship guarantee

Phone No: 0413 586931
email: repairs@bramblefitouts.com.au
Nice to have
• Some sort of image or background that reflects interior fit out work.

```html
<!DOCTYPE html>
<html lang="en">
<head>
<meta charset="utf-8">
<title>Fitout Care Repairs – Business Card</title>
<link rel="stylesheet" href="https://fonts.googleapis.com/css2?family=Open+Sans:wght@400;600&family=Crimson+Text:wght@400&family=Parisienne&display=swap">
<style>
  :root {
    --page-bg: #e9e7e4;
    --card-blue: #2f3893;
    --accent-red: #e53a25;
    --white: #ffffff;
    --gold: #f2c318;
    --gold-dark: #c99a0c;
    --photo-steel: #3f4f76;
    --photo-wood: #b89372;
    --photo-ceiling: #d8c7a6;
    --bullet-ring: #9aa3d8;
  }
  * { box-sizing: border-box; margin: 0; padding: 0; }
  html, body { width: 1200px; height: 740px; overflow: hidden; }
  body {
    background: var(--page-bg);
    position: relative;
    font-family: "Open Sans", Arial, sans-serif;
  }
  .card {
    position: absolute;
    top: 205px;
    width: 540px;
    height: 330px;
    background: var(--card-blue);
    border: 4px solid var(--white);
    overflow: hidden;
    box-shadow: 0 6px 18px rgba(0,0,0,0.18);
  }
  .card--front { left: 30px; }
  .card--back { left: 630px; }

  /* Front */
  .title-band {
    position: absolute; left: 0; top: 0; width: 100%; height: 72px;
    border-bottom: 3px solid var(--white);
    display: flex; align-items: center; padding-left: 26px;
  }
  .title {
    color: var(--white); font-weight: 400; font-size: 35px; letter-spacing: -0.5px;
    white-space: nowrap;
  }
  .photo-row {
    position: absolute; left: 0; top: 75px; width: 100%; height: 118px;
    display: flex; gap: 4px; background: var(--white); padding: 4px 0;
  }
  .photo { flex: 1; }
  .photo--welding { background: linear-gradient(135deg, #1d2440, var(--photo-steel) 60%, #a9b6d6); }
  .photo--joinery { background: linear-gradient(160deg, #cfc4b8, var(--photo-wood) 55%, #7b5c4a); }
  .photo--drilling { background: linear-gradient(150deg, #efe6d3, var(--photo-ceiling) 50%, #8c7a62); }
  .division-band {
    position: absolute; left: 0; top: 193px; width: 100%; height: 80px;
    border-top: 3px solid var(--white);
    display: flex; align-items: center; justify-content: center;
  }
  .division {
    font-family: "Parisienne", cursive; color: var(--white); font-size: 26px;
    white-space: nowrap;
  }
  .red-band {
    position: absolute; left: 0; bottom: 0; width: 100%; height: 50px;
    background: var(--accent-red);
  }

  /* Back */
  .guarantee-seal { position: absolute; right: 30px; top: 20px; width: 84px; height: 84px; }
  .services-heading {
    position: absolute; left: 38px; top: 40px;
    font-family: "Crimson Text", Georgia, serif; font-size: 24px; font-weight: 400;
    color: var(--accent-red);
    border-bottom: 2px solid var(--accent-red); padding-bottom: 1px;
  }
  .services {
    position: absolute; left: 38px; top: 86px; list-style: none;
    font-family: "Crimson Text", Georgia, serif; color: var(--white);
    font-size: 22px; line-height: 30px;
  }
  .services li { display: flex; align-items: center; gap: 10px; }
  .services li::before {
    content: ""; width: 13px; height: 13px; border-radius: 50%;
    background: var(--white); border: 2px solid var(--bullet-ring); flex: none;
  }
  .contact-band {
    position: absolute; left: 0; bottom: 0; width: 100%; height: 54px;
    background: var(--accent-red);
    display: flex; align-items: center; justify-content: space-between;
    padding: 0 22px;
    font-family: "Parisienne", cursive; color: var(--white);
  }
  .contact-item { display: flex; align-items: center; gap: 10px; white-space: nowrap; }
  .contact-phone { font-size: 25px; }
  .contact-email { font-size: 21px; }
  .contact-icon { width: 26px; height: 26px; flex: none; }
</style>
</head>
<body>

<section class="card card--front" aria-label="Business card front">
  <header class="title-band">
    <h1 class="title">Fitout Care Repairs</h1>
  </header>
  <div class="photo-row">
    <div class="photo photo--welding" role="img" aria-label="Photo of a tradesman welding metalwork"></div>
    <div class="photo photo--joinery" role="img" aria-label="Photo of a joiner working on a timber fixture"></div>
    <div class="photo photo--drilling" role="img" aria-label="Photo of a drill fixing a ceiling panel"></div>
  </div>
  <div class="division-band">
    <p class="division">A division of Bramble Fitouts Australia Pty Ltd</p>
  </div>
  <div class="red-band"></div>
</section>

<section class="card card--back" aria-label="Business card back">
  <svg class="guarantee-seal" viewBox="0 0 84 84" role="img" aria-label="Workmanship guarantee seal">
    <circle cx="42" cy="42" r="40" fill="var(--gold)"/>
    <circle cx="42" cy="42" r="30" fill="none" stroke="var(--gold-dark)" stroke-width="2"/>
  </svg>
  <h2 class="services-heading">Our Services</h2>
  <ul class="services">
    <li>Joinery metalwork and fixture repairs</li>
    <li>Patching and painting</li>
    <li>Lighting replacement</li>
    <li>20 years experience</li>
    <li>Fully insured</li>
  </ul>
  <footer class="contact-band">
    <div class="contact-item">
      <svg class="contact-icon" viewBox="0 0 26 26" aria-hidden="true">
        <rect x="1" y="1" width="24" height="24" rx="5" fill="var(--white)"/>
        <path d="M8 6c1 0 2 2.5 2 3.2 0 .8-1.2 1.2-1 2 .6 2 2.5 4 4.6 4.7.8.2 1.2-1 2-1 .7 0 3.2 1 3.2 2s-1.5 2.6-3 2.6C10.5 19.5 6 14.5 6 9.3 6 7.5 7 6 8 6z" fill="var(--accent-red)"/>
      </svg>
      <span class="contact-phone">0413 586931</span>
    </div>
    <div class="contact-item">
      <svg class="contact-icon" viewBox="0 0 26 26" aria-hidden="true">
        <rect x="1" y="5" width="24" height="16" fill="none" stroke="var(--white)" stroke-width="2"/>
        <path d="M1 5l12 9 12-9" fill="none" stroke="var(--white)" stroke-width="2"/>
      </svg>
      <span class="contact-email">repairs@bramblefitouts.com.au</span>
    </div>
  </footer>
</section>

</body>
</html>
```